Clear Summit Vitality Label Designs

I am looking for a label design for my supplements called "Clear Summit Vitality." I am looking for a label that is contemporary, and gender-neutral and that fits well with my product logo. I have 50 products so it would have to be versatile enough to change out the product names.
Choose the labels that fit best. NHB, GMP, third party tested, USA the most important.
Colors chosen are points of reference, be creative, have fun.

Target Market(s)

health minded consumers. Both men and women, so gender neutral.

Colors
9bcb3c
3176b5

Requirements
Must have
• Coloring that is in line with my logo. Contempory. Stamdard supplent panel for ingrsupplement facts, suggested use, general safety, disclaimers, logo, small decals for NHB, GMP, etc, I can provide them if necessary, lot # expiration date, lot number,

```html
<!DOCTYPE html>
<html lang="en">
<head>
<meta charset="utf-8">
<title>Clear Summit Vitality – Supplement Label</title>
<link rel="stylesheet" href="https://fonts.googleapis.com/css2?family=Roboto+Condensed:wght@400;700&family=Open+Sans:wght@400;600&family=Arimo:wght@400;700&display=swap">
<style>
  :root {
    --page: #f4f4f4;
    --label-dark: #151617;
    --green: #79c24e;
    --green-deep: #4f9a35;
    --blue: #2f8fd3;
    --white: #ffffff;
    --text-soft: #e6e6e6;
  }
  * { box-sizing: border-box; margin: 0; padding: 0; }
  html, body { width: 1125px; height: 1200px; overflow: hidden; background: var(--page); }
  .label {
    position: absolute; left: 30px; top: 400px; width: 1065px; height: 398px;
    background: var(--label-dark); color: var(--white);
    font-family: "Open Sans", sans-serif;
    box-shadow: 0 8px 18px rgba(0,0,0,.35);
    overflow: hidden;
  }
  .abs { position: absolute; }
  .accent { color: var(--blue); }

  /* left panel */
  .usage { left: 36px; top: 33px; width: 261px; font-size: 8.3px; line-height: 1.3; text-align: justify; color: var(--text-soft); }
  .usage p + p { margin-top: 7px; }
  .keep-out { left: 38px; top: 154px; width: 259px; height: 40px; background: var(--green); display: flex; align-items: center; justify-content: center; text-align: center; font-family: "Roboto Condensed", sans-serif; font-size: 10.5px; line-height: 1.25; color: var(--white); }
  .allergen { left: 36px; top: 206px; width: 261px; text-align: center; font-size: 7.6px; line-height: 1.35; color: var(--text-soft); }
  .disclaimer { left: 38px; top: 241px; width: 259px; height: 47px; border: 1px solid #bdbdbd; padding: 6px 11px; font-size: 7.7px; line-height: 1.35; color: var(--text-soft); }

  /* center panel */
  .brand { left: 360px; top: 38px; width: 270px; display: flex; align-items: center; justify-content: center; gap: 7px; white-space: nowrap; font-family: "Roboto Condensed", sans-serif; font-weight: 700; font-size: 26px; line-height: 1; color: var(--green); }
  .brand-dot { width: 14px; height: 14px; border-radius: 50%; background: var(--blue); flex: none; }
  .product-name { left: 340px; top: 103px; width: 300px; text-align: center; font-family: "Roboto Condensed", sans-serif; font-weight: 700; line-height: .98; letter-spacing: -1px; }
  .product-name .line-1 { display: block; font-size: 66px; color: var(--white); }
  .product-name .line-2 { display: block; font-size: 66px; color: var(--green); }
  .type-bar { left: 366px; top: 241px; width: 257px; height: 26px; border-radius: 3px; background: linear-gradient(90deg, #bdbdbd, #ffffff 50%, #bdbdbd); color: #1b1b1b; display: flex; align-items: center; justify-content: center; font-family: "Roboto Condensed", sans-serif; font-weight: 700; font-size: 16px; letter-spacing: 5px; }
  .benefits { left: 360px; top: 292px; list-style: none; font-family: "Roboto Condensed", sans-serif; font-size: 18px; color: var(--white); }
  .benefits li { display: flex; align-items: center; height: 26.5px; }
  .benefits svg { width: 22px; height: 18px; margin-right: 18px; }

  /* badge strip */
  .badge-strip { left: 651px; top: 0; width: 73px; height: 292px; background: var(--green); border-radius: 0 0 36px 36px; }
  .seal { position: absolute; left: 11px; width: 51px; height: 51px; border-radius: 50%; background: var(--white); border: 4px solid var(--green-deep); }
  .seal.blue { border-color: var(--blue); background: #e8f2fb; }
  .seal.olive { background: #dcefc9; border-color: #3f7d2a; }
  .count { left: 653px; top: 318px; width: 69px; height: 63px; background: var(--green); border-radius: 18px 18px 0 0; text-align: center; font-family: "Roboto Condensed", sans-serif; font-weight: 700; color: var(--white); }
  .count .number { display: block; font-size: 36px; line-height: 40px; }
  .count .unit { display: block; font-weight: 400; font-size: 13px; line-height: 14px; }

  /* right panel */
  .facts { left: 814px; top: 24px; width: 191px; height: 213px; border: 1.5px solid var(--white); padding: 4px 5px; font-family: "Arimo", sans-serif; color: var(--white); font-size: 7px; line-height: 1.2; }
  .facts h2 { font-size: 15px; font-weight: 700; text-align: center; line-height: 1.1; }
  .facts .serving { font-weight: 700; font-size: 7.2px; border-bottom: 3px solid var(--white); padding-bottom: 3px; }
  .facts .head { text-align: right; font-weight: 700; font-size: 6.5px; border-bottom: 1.5px solid var(--white); padding: 2px 0; }
  .row { display: grid; grid-template-columns: 1fr 46px 20px; border-bottom: .5px solid #888; }
  .row span:nth-child(2), .row span:nth-child(3) { text-align: right; }
  .row .indent-1 { padding-left: 7px; }
  .row .indent-2 { padding-left: 12px; }
  .facts .foot { border-top: 3px solid var(--white); margin-top: 2px; padding-top: 2px; font-size: 6.8px; }
  .ingredients { left: 781px; top: 260px; width: 256px; text-align: center; font-size: 8.8px; line-height: 1.4; color: var(--text-soft); }
  .origin-seal { left: 784px; top: 320px; width: 32px; height: 32px; border-radius: 50%; background: var(--white); border: 3px solid #c9c9c9; }
  .recycle { left: 828px; top: 321px; width: 30px; height: 30px; }
  .maker { left: 869px; top: 314px; width: 161px; height: 43px; border: 1px solid #bdbdbd; text-align: center; font-size: 8.8px; color: var(--text-soft); padding-top: 16px; }
  .maker-title { position: absolute; top: -6px; left: 50%; transform: translateX(-50%); background: var(--label-dark); padding: 0 6px; font-family: "Roboto Condensed", sans-serif; font-weight: 700; font-size: 8.5px; color: var(--green); white-space: nowrap; }

  .base-band { left: 0; bottom: 0; width: 100%; height: 18px; background: linear-gradient(90deg, var(--blue), var(--green)); }
</style>
</head>
<body>
<main class="label">
  <!-- left panel -->
  <section class="usage abs">
    <p><span class="accent">Suggested Use:</span> Lorem Ipsum is simply dummy text of the printing and typesetting industry. Lorem Ipsum has been the industry's standard dummy text ever since the 1500s, when an unknown printer took a galley of type and scrambled it to make a type specimen book.</p>
    <p><span class="accent">Caution:</span> Lorem Ipsum is simply dummy text of the printing and typesetting industry. Lorem Ipsum has been the industry's standard dummy text ever since the 1500s, when an unknown printer took a galley of type and scrambled it to make a type specimen book.</p>
  </section>
  <div class="keep-out abs">KEEP OUT OF REACH OF CHILDREN.<br>STORE AT ROOM TEMPERATURE.</div>
  <p class="allergen abs"><span class="accent">ALLERGEN WARNING:</span> Lorem Ipsum is simply dummy text of the printing and typesetting industry.</p>
  <p class="disclaimer abs"><span class="accent">NHB Warning:</span> These statements have not been evaluated by the National Health Board. This product is not intended to diagnose, treat, cure or prevent any disease.</p>

  <!-- center panel -->
  <header class="brand abs"><span class="brand-dot"></span>Clear Summit Vitality</header>
  <h1 class="product-name abs"><span class="line-1">PRODUCT</span><span class="line-2">NAME</span></h1>
  <div class="type-bar abs">DIETARY SUPPLEMENT</div>
  <ul class="benefits abs">
    <li><svg viewBox="0 0 22 18"><path d="M11 17V9M11 9C8 4 4 3 1 4c1 4 5 6 10 5zM11 9c3-5 7-6 10-5-1 4-5 6-10 5z" fill="none" stroke="#79c24e" stroke-width="1.8"/></svg>Detox &amp; Gut Health</li>
    <li><svg viewBox="0 0 22 18"><path d="M11 17V9M11 9C8 4 4 3 1 4c1 4 5 6 10 5zM11 9c3-5 7-6 10-5-1 4-5 6-10 5z" fill="none" stroke="#79c24e" stroke-width="1.8"/></svg>Immune Health</li>
    <li><svg viewBox="0 0 22 18"><path d="M11 17V9M11 9C8 4 4 3 1 4c1 4 5 6 10 5zM11 9c3-5 7-6 10-5-1 4-5 6-10 5z" fill="none" stroke="#79c24e" stroke-width="1.8"/></svg>Weight Management</li>
  </ul>

  <aside class="badge-strip abs">
    <div class="seal" style="top:33px" role="img" aria-label="Organic certification badge"></div>
    <div class="seal blue" style="top:97px" role="img" aria-label="Registered facility badge"></div>
    <div class="seal olive" style="top:165px" role="img" aria-label="Third party lab tested badge"></div>
    <div class="seal blue" style="top:232px" role="img" aria-label="Good manufacturing practice badge"></div>
  </aside>
  <div class="count abs"><span class="number">90</span><span class="unit">VEGE CAPS</span></div>

  <!-- right panel -->
  <section class="facts abs">
    <h2>Supplement Facts</h2>
    <div class="serving">Serving Size: 1 Gummy<br>Servings Per Container: 60</div>
    <div class="head">Amount Per Serving &nbsp;% DV</div>
    <div class="row"><span>Calories</span><span>10</span><span></span></div>
    <div class="row"><span>Total Carbohydrates</span><span>3 g</span><span>&lt;1%</span></div>
    <div class="row"><span class="indent-1">Total Sugars</span><span>2 g</span><span>**</span></div>
    <div class="row"><span class="indent-2">Includes 2 g Added Sugars</span><span></span><span>4%</span></div>
    <div class="row"><span>Vitamin B-6 (as Pyridoxine HCl)</span><span>0.5 mg</span><span>29%</span></div>
    <div class="row"><span>Folate (120 mcg Folic Acid)</span><span>200 mcg DFE</span><span>50%</span></div>
    <div class="row"><span>Vitamin B-12 (as Cyanocobalamin)</span><span>1.2 mcg</span><span>50%</span></div>
    <div class="row"><span>Iodine (as Potassium Iodide)</span><span>50 mcg</span><span>33%</span></div>
    <div class="row"><span>Apple Cider Vinegar Powder (fruit)<br>(providing 5% total acid)</span><span>500 mg</span><span>**</span></div>
    <div class="row"><span>Pomegranate Juice Powder</span><span>40 mcg</span><span>**</span></div>
    <div class="row"><span>Beet Root Juice Powder</span><span>40 mcg</span><span>**</span></div>
    <div class="foot">* % Daily Value Based on 2,000 Calorie Diet<br>** Daily Value Not Established</div>
  </section>
  <p class="ingredients abs"><span class="accent">Other Ingredients:</span> Lorem Ipsum is simply dummy text of the printing and typesetting industry. Lorem Ipsum has been the industry's standard dummy text ever since the 1500s,</p>
  <div class="origin-seal abs" role="img" aria-label="Country of origin quality badge"></div>
  <svg class="recycle abs" viewBox="0 0 30 30" role="img" aria-label="Recyclable">
    <g fill="none" stroke="#ffffff" stroke-width="3" stroke-linejoin="round" stroke-linecap="round">
      <path d="M12 5l3-3 5 8"/><path d="M24 14l4 8H19"/><path d="M11 27H3l4-8"/>
    </g>
    <g fill="#ffffff">
      <path d="M17 11l6-2-1 6z"/><path d="M20 19l-4 3 4 3z"/><path d="M4 15l3 5 3-4z"/>
    </g>
  </svg>
  <div class="maker abs"><span class="maker-title">MANUFACTURED FOR:</span>Manufactured for Zone</div>

  <div class="base-band abs"></div>
</main>
</body>
</html>
```